Mesh Banner Design for Business Premises

We require the design of a large mesh banner to be installed across the front fence of our warehouse. The banner should prominently feature our existing Trelborn logo and brand colours (yellow, white, and black) and be designed to be highly visible from the road.

The overall aesthetic should be strong, masculine, and industrial, reflecting the nature of the scaffolding and construction industry. The background should be predominantly black, with our branding incorporated in yellow and white for strong contrast and readability.

The banner should clearly communicate the full scope of services we provide, including:

Scaffold Design
Scaffold Engineering
Scaffold Installation / Erection
Scaffold Dismantling

It should also indicate the types of projects and clients we service, including:

Commercial
Industrial
Residential
Civil

The design should feel bold and professional, with a construction-oriented style that aligns with the scaffolding industry. It should be clean, impactful, and easy to read from a distance, ensuring passing traffic can quickly understand our services.

Where possible, subtle industrial or structural design elements (such as scaffold components, steel textures, or linework) may be incorporated into the background to reinforce the industry theme while keeping the layout uncluttered.

The final design will be produced as a large-format mesh banner for outdoor installation, so it should be created with this application and viewing distance in mind.

```html
<!DOCTYPE html>
<html lang="en">
<head>
<meta charset="utf-8">
<title>Trelborn Scaffolding Experts – Fence Banner</title>
<link rel="stylesheet" href="https://fonts.googleapis.com/css2?family=Bebas+Neue&family=Michroma&family=Montserrat:wght@800;900&display=swap">
<style>
  :root {
    --banner-black: #000000;
    --brand-yellow: #f9c013;
    --brand-white: #ffffff;
  }
  * { box-sizing: border-box; margin: 0; padding: 0; }
  html, body {
    width: 1200px;
    height: 250px;
    overflow: hidden;
    background: var(--banner-black);
  }
  .banner {
    position: relative;
    width: 1200px;
    height: 250px;
    background: var(--banner-black);
    overflow: hidden;
  }
  .brand-mark {
    position: absolute;
    left: 40px;
    top: 44px;
    width: 120px;
    height: 96px;
  }
  .brand-lockup {
    position: absolute;
    left: 200px;
    top: 30px;
    width: 664px;
    height: 120px;
  }
  .brand-name {
    font-family: "Michroma", sans-serif;
    font-size: 52px;
    fill: var(--brand-white);
  }
  .tagline-pill { fill: var(--brand-yellow); }
  .tagline {
    font-family: "Bebas Neue", sans-serif;
    font-size: 50px;
    fill: var(--banner-black);
  }
  .services {
    position: absolute;
    left: 21px;
    top: 175px;
    width: 850px;
    display: grid;
    grid-template-columns: 523px auto;
    row-gap: 8px;
    list-style: none;
    font-family: "Montserrat", sans-serif;
    font-weight: 900;
    font-size: 22px;
    line-height: 25px;
    color: var(--brand-white);
    white-space: nowrap;
  }
  .services .keyword,
  .services .dash { color: var(--brand-yellow); }
  .divider {
    position: absolute;
    left: 890px;
    top: 24px;
    width: 7px;
    height: 203px;
    background: linear-gradient(to bottom, var(--brand-yellow) 0 49%, var(--brand-white) 49% 100%);
  }
  .sectors-heading {
    position: absolute;
    left: 910px;
    top: 37px;
    width: 290px;
    height: 38px;
    background: var(--brand-yellow);
    color: var(--banner-black);
    font-family: "Bebas Neue", sans-serif;
    font-size: 38px;
    line-height: 40px;
    padding-left: 12px;
    letter-spacing: 0.2px;
    white-space: nowrap;
  }
  .sectors {
    position: absolute;
    left: 915px;
    top: 95px;
    list-style: none;
    font-family: "Montserrat", sans-serif;
    font-weight: 900;
    font-size: 22px;
    line-height: 33.4px;
    color: var(--brand-yellow);
  }
</style>
</head>
<body>
<main class="banner">
  <svg class="brand-mark" viewBox="0 0 120 96" aria-hidden="true">
    <rect x="12" y="0" width="96" height="96" fill="none" stroke="#f9c013" stroke-width="6"/>
  </svg>

  <svg class="brand-lockup" viewBox="0 0 664 120" aria-label="Trelborn – Scaffolding Experts">
    <text class="brand-name" x="8" y="47" textLength="652" lengthAdjust="spacing">TRELBORN</text>
    <rect class="tagline-pill" x="1" y="64" width="660" height="52" rx="18"/>
    <text class="tagline" x="23" y="107" textLength="614" lengthAdjust="spacing">SCAFFOLDING EXPERTS</text>
  </svg>

  <ul class="services">
    <li><span class="dash">-</span> <span class="keyword">SCAFFOLD</span> DESIGN</li>
    <li><span class="dash">-</span> <span class="keyword">SCAFFOLD</span> ENGINEERING</li>
    <li><span class="dash">-</span> <span class="keyword">SCAFFOLD</span> INSTALLATION / ERECTION</li>
    <li><span class="dash">-</span> <span class="keyword">SCAFFOLD</span> DISMANTLING</li>
  </ul>

  <div class="divider" aria-hidden="true"></div>

  <h2 class="sectors-heading">SERVING ALL SECTORS</h2>
  <ul class="sectors">
    <li>- COMMERCIAL</li>
    <li>- INDUSTRIAL</li>
    <li>- RESIDENTIAL</li>
    <li>- CIVIL</li>
  </ul>
</main>
</body>
</html>
```